Marcus Feldwick Carpentry & Joinery

Hello, I would like a flyer designed for my new business doing small projects in my local area for home-owners. I am a professional tradesman.
The type of work I am offering is:
- decks/decking
- external stairs & railings
- install windows & doors
- roofs & gutters
- small additions
- built-in wardrobes
- finish work
- demolition

It would be great if the flyer could mention these, or use phrasing that fits this kind of construction work.
My idea for a slogan was "new work and repairs to any age home".

Please also mention FREE QUOTES and have my email and phone number included on the flyer, along with my carpentry licence number, which I can provided.

I'd like a one page, single-sided flyer that could be printed as DL.
Colour and style is up to you! I'll be placing this flyer on counters & in the windows of local businesses, so something simple and eye-catching is preferred.

Thank you!

```html
<!DOCTYPE html>
<html lang="en">
<head>
<meta charset="utf-8">
<title>Marcus Feldwick Carpentry &amp; Joinery – DL Flyer</title>
<link href="https://fonts.googleapis.com/css2?family=Amaranth:wght@400;700&family=Philosopher:wght@400;700&family=Yanone+Kaffeesatz:wght@300;400&display=swap" rel="stylesheet">
<style>
  :root {
    --page-bg: #e4e2df;
    --panel-bg: #f3f3f3;
    --brand-blue: #33a6dc;
    --badge-blue: #2f8fca;
    --text-brown: #5b4a40;
    --rule-brown: #8c7a6e;
    --white: #ffffff;
    --deck-tone: linear-gradient(135deg, #8d7460 0%, #b39a80 55%, #cfb37d 100%);
    --stairs-tone: linear-gradient(160deg, #e9e7e3 0%, #c27550 50%, #9b7d6c 100%);
    --window-tone: linear-gradient(120deg, #d8d6d0 0%, #b9bcb5 50%, #8fa58a 100%);
    --roof-tone: linear-gradient(150deg, #6d6f72 0%, #47494c 60%, #8a7a6c 100%);
  }
  * { box-sizing: border-box; margin: 0; padding: 0; }
  html, body { width: 1200px; height: 660px; overflow: hidden; background: var(--page-bg); }
  .flyer {
    position: absolute; left: 30px; top: 59px;
    width: 1140px; height: 542px;
    background: var(--white);
    box-shadow: 0 4px 14px rgba(0,0,0,0.18);
    overflow: hidden;
  }
  .photo-grid {
    position: absolute; left: 0; top: 0; width: 586px; height: 542px;
    display: grid; grid-template-columns: 290px 292px; grid-template-rows: 266px 272px;
    gap: 4px; background: var(--white);
  }
  .photo { width: 100%; height: 100%; }
  .photo--deck { background: var(--deck-tone); }
  .photo--stairs { background: var(--stairs-tone); }
  .photo--window { background: var(--window-tone); }
  .photo--roof { background: var(--roof-tone); }
  .guarantee-badge { position: absolute; left: 212px; top: 186px; width: 222px; height: 150px; }
  .info-panel {
    position: absolute; left: 586px; top: 0; width: 554px; height: 542px;
    background: var(--panel-bg);
    font-family: "Amaranth", sans-serif; color: var(--text-brown);
  }
  .business-name {
    position: absolute; right: 34px; top: 34px; text-align: right;
    font-family: "Philosopher", sans-serif; font-weight: 400;
    font-size: 30px; line-height: 34px; color: var(--brand-blue);
  }
  .slogan {
    position: absolute; left: 26px; top: 139px; width: 482px; height: 52px;
    border-top: 2px solid var(--rule-brown); border-bottom: 2px solid var(--rule-brown);
    font-size: 26px; line-height: 48px; font-weight: 400; color: var(--text-brown);
    white-space: nowrap; letter-spacing: -0.2px;
  }
  .services-heading {
    position: absolute; left: 40px; top: 216px;
    font-family: "Yanone Kaffeesatz", sans-serif; font-weight: 400;
    font-size: 27px; color: var(--brand-blue); display: flex; align-items: center; gap: 8px;
  }
  .services-heading svg { width: 19px; height: 19px; }
  .service-list {
    position: absolute; top: 260px; list-style: none;
    font-family: "Yanone Kaffeesatz", sans-serif; font-weight: 400; font-size: 25px; line-height: 37.5px;
    color: var(--text-brown);
  }
  .service-list--left { left: 67px; }
  .service-list--right { left: 343px; }
  .service-list li::before { content: "» "; }
  .licence {
    position: absolute; right: 38px; top: 434px;
    font-family: "Yanone Kaffeesatz", sans-serif; font-size: 19px; color: var(--text-brown);
  }
  .contact-band {
    position: absolute; left: 44px; top: 462px; right: 0; height: 80px;
    background: var(--brand-blue); border-top-left-radius: 40px;
    color: var(--white); font-family: "Yanone Kaffeesatz", sans-serif; text-align: center;
    padding-left: 10px;
  }
  .contact-band__call {
    margin-top: 8px; font-size: 23px; display: flex; justify-content: center; align-items: center; gap: 10px;
  }
  .contact-band__call svg { width: 22px; height: 22px; }
  .contact-band__phone { font-size: 24px; }
  .contact-band__email { font-size: 17px; margin-top: 2px; }
</style>
</head>
<body>
  <main class="flyer">
    <section class="photo-grid">
      <div class="photo photo--deck" role="img" aria-label="Weathered timber deck boards with new replacement boards"></div>
      <div class="photo photo--stairs" role="img" aria-label="Timber staircase with railings in a bright interior"></div>
      <div class="photo photo--window" role="img" aria-label="Tradesman with tool belt installing a window"></div>
      <div class="photo photo--roof" role="img" aria-label="Shingle roof edge and gutter with fallen leaves"></div>
    </section>

    <svg class="guarantee-badge" viewBox="0 0 222 150" aria-label="100% Satisfaction Guarantee">
      <circle cx="111" cy="74" r="70" fill="#ffffff"/>
      <circle cx="111" cy="74" r="64" fill="none" stroke="var(--badge-blue)" stroke-width="5"/>
      <text x="111" y="60" text-anchor="middle" font-family="Philosopher, serif" font-weight="700" font-size="32" fill="var(--badge-blue)">100%</text>
      <path d="M4 98 L30 84 L30 122 L4 126 L18 110 Z" fill="#1f6fa3"/>
      <path d="M218 98 L192 84 L192 122 L218 126 L204 110 Z" fill="#1f6fa3"/>
      <path d="M22 76 Q111 56 200 76 L200 110 Q111 90 22 110 Z" fill="var(--badge-blue)"/>
      <text x="111" y="95" text-anchor="middle" font-family="Amaranth, sans-serif" font-size="21" fill="#ffffff">Satisfaction</text>
      <text x="111" y="122" text-anchor="middle" font-family="Amaranth, sans-serif" font-size="11" fill="var(--badge-blue)">GUARANTEE</text>
    </svg>

    <section class="info-panel">
      <h1 class="business-name">Marcus Feldwick<br>Carpentry &amp; Joinery</h1>
      <p class="slogan">New Work and Repairs to any age home!</p>
      <h2 class="services-heading">
        <svg viewBox="0 0 20 20" aria-hidden="true"><circle cx="10" cy="10" r="10" fill="var(--brand-blue)"/><path d="M8 5.5 L12.5 10 L8 14.5" fill="none" stroke="#fff" stroke-width="2.4"/></svg>
        Services:
      </h2>
      <ul class="service-list service-list--left">
        <li>decks/decking</li>
        <li>external stairs &amp; railings</li>
        <li>install windows &amp; doors</li>
        <li>roofs &amp; gutters</li>
      </ul>
      <ul class="service-list service-list--right">
        <li>small additions</li>
        <li>built-in wardrobes</li>
        <li>finish work</li>
        <li>demolition</li>
      </ul>
      <p class="licence">Licence number: 1458203</p>
      <div class="contact-band">
        <p class="contact-band__call">Call us now for a FREE QUOTES:
          <svg viewBox="0 0 24 24" aria-hidden="true"><circle cx="12" cy="12" r="10.5" fill="none" stroke="#fff" stroke-width="2"/><path d="M8.2 6.5 L10 6.3 L11 9 L9.8 10.1 Q10.8 12.6 13.2 13.9 L14.3 12.8 L17 13.8 L16.8 15.6 Q15.6 17 13.8 16.6 Q8.5 14.8 7 9.8 Q6.8 7.6 8.2 6.5 Z" fill="#fff"/></svg>
          <span class="contact-band__phone">0412 558 903</span>
        </p>
        <p class="contact-band__email">email: marcusfeldwick@mailbox.net mobile</p>
      </div>
    </section>
  </main>
</body>
</html>
```